Bruntel general construction

We need an website that are similar to these websites:
https://www.morvexa.com/en/
https://dulnari.com/company/

but with a tweak. Do not copy the entire website but atleast similar and yet better than them.

For reference this our current website.
https://bruntel.ph/

For the winning Designer please help us with the migration from our old website to the new redesign website.

```html
<!DOCTYPE html>
<html lang="en">
<head>
<meta charset="utf-8">
<title>Bruntel — General Construction</title>
<link rel="stylesheet" href="https://fonts.googleapis.com/css2?family=Lexend:wght@400;500;600&family=Lato:wght@400;700&display=swap">
<style>
:root{
  --blue:#1a8fe3;
  --slate:#34495a;
  --slate-dark:#2c3e4d;
  --ink:#333a40;
  --muted:#555d63;
  --line:#c9ced3;
  --orange:#f26a1b;
  --yellow:#ffd400;
  --white:#fff;
}
*{box-sizing:border-box;margin:0;padding:0}
html,body{width:1200px;height:2451px;overflow:hidden;background:var(--white)}
body{position:relative;font-family:"Lato",sans-serif;color:var(--ink)}
.abs{position:absolute}
h1,h2,h3,.display{font-family:"Lexend",sans-serif}

/* hero */
.hero{left:0;top:0;width:1200px;height:690px;background:var(--slate);overflow:hidden}
.hero-photo{left:560px;top:60px;width:640px;height:520px;background:linear-gradient(135deg,#6b7784 0%,#d8c24a 45%,#f3e07a 60%,#7b8793 100%);clip-path:polygon(18% 0,100% 0,100% 100%,0 100%,0 45%)}
.hero-text{left:120px;top:240px;width:470px;font-family:"Lexend",sans-serif;font-weight:400;font-size:21px;line-height:33.5px;color:var(--white)}
.hero-arrow{width:30px;height:30px;border-radius:50%;background:var(--orange);display:flex;align-items:center;justify-content:center}
.hero-waves{left:0;top:460px}

/* header */
.site-header{left:64px;top:0;width:1072px;height:85px;background:var(--white);clip-path:polygon(0 0,100% 0,97% 100%,3% 100%)}
.brand{left:119px;top:20px;display:flex;align-items:center;gap:6px}
.brand-dot{width:14px;height:14px;border-radius:50%;background:var(--orange)}
.brand-name{font-family:"Lexend",sans-serif;font-weight:600;font-size:16px;color:var(--blue)}
.nav{top:38px;display:flex;gap:24px;left:552px;font-family:"Lexend",sans-serif;font-size:13px;color:#333}
.nav a{color:inherit;text-decoration:none}
.nav .active{border-bottom:2px solid var(--blue);padding-bottom:4px}
.nav-cta{left:983px;top:33px;width:97px;height:28px;background:var(--blue);color:var(--white);border-radius:3px;font-family:"Lexend",sans-serif;font-size:13px;display:flex;align-items:center;justify-content:center}

/* expertise */
.section-title{font-family:"Lexend",sans-serif;font-weight:500;color:var(--blue);font-size:50px;line-height:52px}
.expertise-title{left:119px;top:668px}
.expertise-intro{left:624px;top:673px;width:455px;font-size:15px;line-height:20px;color:#333}
.card{width:222px;height:370px;top:814px;border:1px solid var(--line);border-radius:12px;text-align:center;overflow:hidden}
.card-photo{margin:4px;height:106px;border-radius:3px 3px 0 0}
.card h3{font-family:"Lexend",sans-serif;font-weight:500;font-size:14.5px;line-height:20px;color:var(--blue);margin:14px 18px 0;padding-bottom:8px;border-bottom:1px solid var(--blue)}
.card p{font-size:13px;line-height:19px;color:#444;margin:14px 12px 0;height:136px}
.btn{display:inline-flex;align-items:center;gap:6px;height:22px;padding:0 7px;border:1px solid var(--blue);border-radius:2px;color:var(--blue);font-size:13px;font-family:"Lato",sans-serif}
.btn.solid{background:var(--blue);color:var(--white)}
.card .btn{margin-top:9px}
.dots{left:588px;top:1205px;display:flex;gap:6px}
.dots span{width:9px;height:9px;border-radius:50%;border:1px solid #888}
.dots span.on{border-color:var(--orange);background:radial-gradient(var(--orange) 45%,transparent 50%)}

/* safety band */
.safety{left:0;top:1280px;width:1200px;height:290px;background:var(--slate)}
.safety-photo{left:548px;top:1280px;width:652px;height:290px;background:linear-gradient(160deg,#3e5060 0%,#8896a3 35%,#c9c26a 60%,#4b6aa0 85%,#34495a 100%);clip-path:polygon(30% 0,100% 0,100% 100%,0 100%,0 80%)}
.safety-text{left:120px;top:1374px;width:500px;font-family:"Lexend",sans-serif;font-size:23px;line-height:33px;color:var(--white)}
.safety-text b{font-weight:600}

/* news */
.news-title{left:0;width:1160px;top:1628px;text-align:center}
.news-card{border:1px solid var(--line);border-radius:12px;overflow:hidden}
.news-feature{left:119px;top:1728px;width:458px;height:432px}
.news-feature .photo{height:251px;background:linear-gradient(180deg,#c9cbc8 0%,#a9aaa6 55%,#8a8c86 70%,#d6b63a 85%,#5a3f8c 100%)}
.news-body{padding:0 20px}
.news-date{display:flex;align-items:center;gap:6px;font-size:12.5px;color:#555}
.news-head{font-family:"Lexend",sans-serif;font-weight:500;color:var(--blue);font-size:14.5px;line-height:19px}
.news-ex{font-size:15px;line-height:20px;color:#333}
.news-side{left:623px;width:458px;height:205px}
.news-side .photo{position:absolute;left:10px;top:10px;width:169px;height:181px;border-radius:8px}
.news-side .news-body{position:absolute;left:193px;top:18px;right:4px;padding:0}

/* footer */
.site-footer{left:0;top:2226px;width:1200px;height:225px;background:var(--slate)}
.footer-brand{left:118px;top:2338px;display:flex;align-items:center;gap:8px}
.footer-brand .brand-dot{width:20px;height:20px}
.footer-brand .brand-name{font-size:24px;color:var(--blue)}
.f-head{font-family:"Lexend",sans-serif;font-weight:500;font-size:14.5px;color:var(--white)}
.f-head::after{content:"";display:block;width:30px;height:2px;background:var(--blue);margin-top:8px}
.f-list{font-size:13.5px;line-height:26px;color:var(--white)}
.f-addr{font-size:13px;line-height:17.5px;color:var(--white)}
.f-sep{width:1px;background:rgba(255,255,255,.25);top:2246px;height:110px}
.contact-row{display:flex;align-items:center;gap:8px;font-size:13.5px;line-height:26.5px;color:var(--white)}
.ico{width:14px;height:14px;border-radius:50%;background:var(--blue);display:inline-flex;align-items:center;justify-content:center}
.follow{left:943px;top:2377px;display:flex;align-items:center;gap:7px;color:var(--white);font-family:"Lexend",sans-serif;font-size:13px}
.social{width:17px;height:17px;border-radius:50%;background:var(--blue)}
.f-rule{left:120px;top:2414px;width:960px;height:1px;background:rgba(255,255,255,.55)}
.copyright{left:0;width:1200px;top:2425px;text-align:center;font-size:11px;color:var(--white)}
</style>
</head>
<body>

<!-- Hero -->
<section class="abs hero" aria-label="Hero">
  <div class="abs hero-photo" role="img" aria-label="Offshore oil platform with yellow steel structure"></div>
  <p class="abs hero-text">We support onshore &amp; offshore clientele with a broad range of world-class services &amp; highly trained staff, quality management systems, and exceptional safety performance.</p>
  <div class="abs hero-arrow" style="left:73px;top:285px"><svg width="12" height="14" viewBox="0 0 12 14"><path d="M8 1 2 7l6 6" fill="none" stroke="#fff" stroke-width="1.6"/></svg></div>
  <div class="abs hero-arrow" style="left:1096px;top:285px"><svg width="12" height="14" viewBox="0 0 12 14"><path d="M4 1l6 6-6 6" fill="none" stroke="#fff" stroke-width="1.6"/></svg></div>
  <svg class="abs" style="left:590px;top:476px" width="20" height="26" viewBox="0 0 20 26"><rect x="1" y="1" width="18" height="24" rx="9" fill="none" stroke="#fff" stroke-width="1.3"/><path d="M7 12l3 3 3-3" fill="none" stroke="#fff" stroke-width="1.3"/></svg>
  <svg class="abs hero-waves" width="1200" height="230" viewBox="0 0 1200 230">
    <path d="M0 30 C120 90 230 100 310 110 C200 112 90 95 0 60Z" fill="var(--orange)"/>
    <path d="M0 60 C150 120 300 140 420 130 C560 115 640 60 800 50 C980 40 1120 110 1200 170 V230 H0Z" fill="var(--yellow)"/>
    <path d="M600 90 C800 50 1000 80 1200 190 V230 H600Z" fill="var(--orange)"/>
    <path d="M0 90 C150 150 300 165 430 150 C560 135 640 85 800 78 C970 72 1100 140 1200 210 V230 H0Z" fill="#fff"/>
  </svg>
</section>

<!-- Header -->
<header>
  <div class="abs site-header"></div>
  <div class="abs brand"><span class="brand-dot"></span><span class="brand-name">BRUNTEL</span></div>
  <nav class="abs nav">
    <a class="active" href="#">Home</a><a href="#">About Us</a><a href="#">Our Services</a><a href="#">Our Team</a><a href="#">News &amp; Media</a>
  </nav>
  <a class="abs nav-cta">Contact Us</a>
</header>

<!-- Expertise -->
<section aria-label="Our Expertise">
  <h2 class="abs section-title expertise-title">Our<br>Expertise</h2>
  <p class="abs expertise-intro">Our ability to deliver a quality product has given us the reputation to position ourselves as a leading contractor in the sectors and industries that we serve</p>

  <article class="abs card" style="left:119px">
    <div class="card-photo" role="img" aria-label="Wind turbine on green hills" style="background:linear-gradient(180deg,#5b8fd1 0%,#b9cde0 50%,#5f8a3a 100%)"></div>
    <h3>Environmental Protection<br>and Management</h3>
    <p>We have in-house expertise for the processing of both municipal and industrial solid wastes by adopting the latest technologies. These wastes can be converted to energy in the form of electrical power.</p>
    <span class="btn solid">Read More <svg width="20" height="8" viewBox="0 0 20 8"><path d="M0 4h18M15 1l3 3-3 3" fill="none" stroke="currentColor" stroke-width="1.2"/></svg></span>
  </article>
  <article class="abs card" style="left:365px">
    <div class="card-photo" role="img" aria-label="Power station with cooling towers" style="background:linear-gradient(180deg,#7fa9cc 0%,#d7dde2 55%,#5e6870 100%)"></div>
    <h3>Power<br>Generation</h3>
    <p>We are experienced in the refurbishments of utility, steam raising plant, the repair and maintenance of ancillary equipment from valves to pumps and our experiences in plant shutdown R&amp;M programs.</p>
    <span class="btn">Read More <svg width="20" height="8" viewBox="0 0 20 8"><path d="M0 4h18M15 1l3 3-3 3" fill="none" stroke="currentColor" stroke-width="1.2"/></svg></span>
  </article>
  <article class="abs card" style="left:612px">
    <div class="card-photo" role="img" aria-label="Aerial view of a water treatment plant" style="background:linear-gradient(180deg,#c9a46a 0%,#4e7a3c 40%,#6f8a6a 100%)"></div>
    <h3>Water<br>Treatment</h3>
    <p>We have in-house expertise for the onstruction of Sewage Water Treatment Plants (SWTP) and utility desalination plants for the conversion of seawater to potable water.</p>
    <span class="btn">Read More <svg width="20" height="8" viewBox="0 0 20 8"><path d="M0 4h18M15 1l3 3-3 3" fill="none" stroke="currentColor" stroke-width="1.2"/></svg></span>
  </article>
  <article class="abs card" style="left:858px">
    <div class="card-photo" role="img" aria-label="Oil refinery at dusk" style="background:linear-gradient(180deg,#8a8aa6 0%,#d9a98a 45%,#4a5260 100%)"></div>
    <h3>Oil<br>and Gas</h3>
    <p>We are known in the oil and gas industry for our ability to provide multi skilled, reliable, and cost-effective manpower.</p>
    <span class="btn">Read More <svg width="20" height="8" viewBox="0 0 20 8"><path d="M0 4h18M15 1l3 3-3 3" fill="none" stroke="currentColor" stroke-width="1.2"/></svg></span>
  </article>
  <div class="abs dots"><span class="on"></span><span></span></div>
</section>

<!-- Safety band -->
<section aria-label="Safety statement">
  <div class="abs safety"></div>
  <div class="abs safety-photo" role="img" aria-label="Refinery towers and piping"></div>
  <p class="abs safety-text">OUTSTANDING <b>SAFETY</b>, <b>ENVIRONMENTAL AWARENESS</b>, AND <b>WORLD-CLASS QUALITY DEFINES THE WAY WE WORK</b>.</p>
</section>

<!-- Latest News -->
<section aria-label="Latest News">
  <h2 class="abs section-title news-title">Latest News</h2>

  <article class="abs news-card news-feature">
    <div class="photo" role="img" aria-label="Hazy city waterfront promenade with flower beds"></div>
    <div class="news-body" style="padding-top:22px">
      <div class="news-date"><svg width="11" height="11" viewBox="0 0 11 11"><rect x=".5" y="1.5" width="10" height="9" fill="none" stroke="#555"/><path d="M.5 4h10" stroke="#555"/></svg>October 16, 2017</div>
      <h3 class="news-head" style="margin-top:8px">Environmental Protection Industry A Job Creator</h3>
      <p class="news-ex" style="margin-top:12px">A very different approach is emerging between Australia and China's treatment of jobs and industries providing...</p>
      <span class="btn" style="margin-top:14px">Read More <svg width="20" height="8" viewBox="0 0 20 8"><path d="M0 4h18M15 1l3 3-3 3" fill="none" stroke="currentColor" stroke-width="1.2"/></svg></span>
    </div>
  </article>

  <article class="abs news-card news-side" style="top:1728px">
    <div class="photo" role="img" aria-label="Desalination plant tanks at night" style="background:linear-gradient(180deg,#1d2c4a 0%,#39466a 45%,#b7bcc4 75%,#3a3f48 100%)"></div>
    <div class="news-body">
      <div class="news-date"><svg width="11" height="11" viewBox="0 0 11 11"><rect x=".5" y="1.5" width="10" height="9" fill="none" stroke="#555"/><path d="M.5 4h10" stroke="#555"/></svg>October 17, 2017</div>
      <h3 class="news-head" style="margin-top:8px">Hydrevo To Supply Turbocharger Technology for Saudi Desalination Projects</h3>
      <p class="news-ex" style="margin-top:9px">Hydrevo, a provider of pressure energy technology for...</p>
      <span class="btn" style="margin-top:12px">Read More <svg width="20" height="8" viewBox="0 0 20 8"><path d="M0 4h18M15 1l3 3-3 3" fill="none" stroke="currentColor" stroke-width="1.2"/></svg></span>
    </div>
  </article>

  <article class="abs news-card news-side" style="top:1955px">
    <div class="photo" role="img" aria-label="Oilfield workers at a drilling rig" style="background:linear-gradient(160deg,#8a9aa8 0%,#4d6a9a 45%,#b04a3a 70%,#6e5e4e 100%)"></div>
    <div class="news-body">
      <div class="news-date"><svg width="11" height="11" viewBox="0 0 11 11"><rect x=".5" y="1.5" width="10" height="9" fill="none" stroke="#555"/><path d="M.5 4h10" stroke="#555"/></svg>October 17, 2017</div>
      <h3 class="news-head" style="margin-top:8px">Positive Signs for Oilfield Services Sector as U.S. Onshore Market Set to Grow</h3>
      <p class="news-ex" style="margin-top:9px">Northmere Energy Group, energy market research consultancy...</p>
      <span class="btn" style="margin-top:12px">Read More <svg width="20" height="8" viewBox="0 0 20 8"><path d="M0 4h18M15 1l3 3-3 3" fill="none" stroke="currentColor" stroke-width="1.2"/></svg></span>
    </div>
  </article>
</section>

<!-- Footer -->
<footer>
  <div class="abs site-footer"></div>
  <div class="abs footer-brand"><span class="brand-dot"></span><span class="brand-name">BRUNTEL</span></div>

  <div class="abs" style="left:305px;top:2254px">
    <h4 class="f-head">Quick Links</h4>
    <div style="display:flex;gap:60px;margin-top:8px">
      <div class="f-list">Home<br>About Us<br>Our Services</div>
      <div class="f-list">Our Team<br>News &amp; Media<br>Contact Us</div>
    </div>
  </div>
  <div class="abs f-sep" style="left:553px"></div>

  <div class="abs" style="left:578px;top:2254px">
    <h4 class="f-head">Contact Us:</h4>
    <div style="margin-top:8px">
      <div class="contact-row"><span class="ico"><svg width="8" height="8" viewBox="0 0 8 8"><path d="M1 1.5c0 3 2.5 5.5 5.5 5.5l.5-1.5-1.5-1-1 .8C3.5 5 3 4.5 2.7 3.5l.8-1L2.5 1Z" fill="#fff"/></svg></span>+63 (0) 46 555-0142</div>
      <div class="contact-row"><span class="ico"><svg width="8" height="8" viewBox="0 0 8 8"><path d="M1 1.5c0 3 2.5 5.5 5.5 5.5l.5-1.5-1.5-1-1 .8C3.5 5 3 4.5 2.7 3.5l.8-1L2.5 1Z" fill="#fff"/></svg></span>+63 (0) 43 555-0187</div>
      <div class="contact-row"><span class="ico"><svg width="8" height="6" viewBox="0 0 8 6"><rect x=".5" y=".5" width="7" height="5" fill="none" stroke="#fff"/><path d="M.5 .5 4 3.5 7.5.5" fill="none" stroke="#fff"/></svg></span>info@bruntel.ph</div>
    </div>
  </div>
  <div class="abs f-sep" style="left:745px"></div>

  <div class="abs" style="left:770px;top:2254px">
    <h4 class="f-head">Head Office:</h4>
    <p class="f-addr" style="margin-top:14px">14 Mabini Ave. Brgy. Santol<br>Dasmariñas City, Cavite<br>Philippines 4114</p>
  </div>
  <div class="abs f-sep" style="left:930px"></div>

  <div class="abs" style="left:957px;top:2254px">
    <h4 class="f-head">Satellite Office:</h4>
    <p class="f-addr" style="margin-top:14px">Sitio Malinaw, Brgy.<br>Tabangao Batangas City,<br>Batangas Philippines<br>4200</p>
  </div>

  <div class="abs follow">Follow Us: <span class="social"></span><span class="social"></span><span class="social"></span></div>
  <div class="abs f-rule"></div>
  <p class="abs copyright">Copyright © 2026 Bruntel. All Rights Reserved</p>
</footer>

</body>
</html>
```